Natural/Holistic/Spiritual Product Line ( Body Scrubs, Essential Oils, Lotions, Herbs, Candles, e...

I need Product labels that I can use interchangeably for my company "Marisol Glade" I make natural products such as body scrubs, bath salts, candles, essential oil blends, salves, body butters, etc. I want simple, but elegant labels. I want designs that use green, white and earth tones. My products are all natural, homegrown, handcrafted. Materials are all able to be recycled or are biodegradable.

Target Market(s)

Holistic, Natural, Organic, Herbalism - Body, Mind & Spirit encompassing products

Industry/Entity Type

Skin Care Product

Font styles to use
Sans Serif
Decorative
Script

Colors

Designer to choose colors to be used in the design.

Requirements
Must have
• My logo and simple, elegant designs. I have other logo files I can provide you as well, just ask.
Nice to have
• Surprise me!
Should not have
• Nothing flashy.

```html
<!DOCTYPE html>
<html lang="en">
<head>
<meta charset="utf-8">
<title>Marisol Glade — Product Labels</title>
<link href="https://fonts.googleapis.com/css2?family=Playfair+Display:wght@700;800&family=Yellowtail&display=swap" rel="stylesheet">
<style>
  :root {
    --label-green: #217844;
    --page: #ffffff;
    --white: #ffffff;
    --lavender: #cbb8d9;
    --lavender-leaf: #6d9f89;
    --relief: #86d3a1;
    --relief-leaf: #4ea473;
    --honey: #e5dc8c;
    --honey-leaf: #84a661;
  }
  * { margin: 0; padding: 0; box-sizing: border-box; }
  html, body {
    width: 1200px; height: 1035px; overflow: hidden;
    background: var(--page);
  }
  .sheet { position: relative; width: 1200px; height: 1035px; }
  .label {
    position: absolute;
    background: var(--label-green);
    overflow: hidden;
    color: var(--white);
    font-family: "Playfair Display", Georgia, serif;
    font-weight: 700;
  }
  .label--wide { width: 666px; height: 441px; left: 47px; }
  .label--bath { top: 50px; }
  .label--scrub { top: 543px; }
  .label--rollon { left: 760px; top: 50px; width: 395px; height: 535px; }
  .label--seal { left: 760px; top: 640px; width: 395px; height: 344px; }

  .foliage { position: absolute; top: 0; bottom: 0; width: 140px; }
  .foliage--left { left: 0; }
  .foliage--right { right: 0; }
  .label--bath .foliage--left { background: linear-gradient(90deg, var(--lavender-leaf) 0%, rgba(109,159,137,0.35) 70%, rgba(109,159,137,0) 100%); }
  .label--bath .foliage--right { background: linear-gradient(270deg, var(--lavender-leaf) 0%, rgba(109,159,137,0.35) 70%, rgba(109,159,137,0) 100%); }
  .label--scrub .foliage--left { background: linear-gradient(90deg, var(--honey-leaf) 0%, rgba(132,166,97,0.35) 70%, rgba(132,166,97,0) 100%); }
  .label--scrub .foliage--right { background: linear-gradient(270deg, var(--honey-leaf) 0%, rgba(132,166,97,0.35) 70%, rgba(132,166,97,0) 100%); }
  .label--rollon .foliage { width: 120px; }
  .label--rollon .foliage--left { background: linear-gradient(90deg, var(--relief-leaf) 0%, rgba(78,164,115,0.35) 70%, rgba(78,164,115,0) 100%); }
  .label--rollon .foliage--right { background: linear-gradient(270deg, var(--relief-leaf) 0%, rgba(78,164,115,0.35) 70%, rgba(78,164,115,0) 100%); }

  .line {
    position: absolute; left: 0; right: 0;
    text-align: center; line-height: 1; white-space: nowrap;
  }
  .brand-dot {
    position: absolute; left: 50%;
    width: 22px; height: 22px; margin-left: -11px;
    border-radius: 50%; background: var(--white);
  }
  .brand { font-size: 28px; }
  .product-name { font-family: "Yellowtail", cursive; font-weight: 400; font-size: 62px; }
  .product-type { font-size: 31px; }
  .net-weight { font-size: 25px; }
  .volume { font-size: 18px; }

  .label--bath .product-name { color: var(--lavender); }
  .label--rollon .product-name { color: var(--relief); }
  .label--scrub .product-name { color: var(--honey); font-size: 54px; }
  .label--seal .brand { font-size: 33px; }
</style>
</head>
<body>
<main class="sheet">

  <section class="label label--wide label--bath">
    <div class="foliage foliage--left" role="img" aria-label="Leafy vine illustration along the left edge"></div>
    <div class="foliage foliage--right" role="img" aria-label="Leafy vine illustration along the right edge"></div>
    <span class="brand-dot" style="top:41px"></span>
    <div class="line brand" style="top:86px">Marisol Glade</div>
    <div class="line product-name" style="top:190px">Lavender</div>
    <div class="line product-type" style="top:268px">Bath Salt</div>
    <div class="line net-weight" style="top:381px">Net wt 8 oz</div>
  </section>

  <section class="label label--rollon">
    <div class="foliage foliage--left" role="img" aria-label="Leafy vine illustration along the left edge"></div>
    <div class="foliage foliage--right" role="img" aria-label="Leafy vine illustration along the right edge"></div>
    <span class="brand-dot" style="top:42px"></span>
    <div class="line brand" style="top:91px">Marisol Glade</div>
    <div class="line product-name" style="top:224px">Relief</div>
    <div class="line product-type" style="top:397px; font-size:27px">Essential Oil</div>
    <div class="line product-type" style="top:428px; font-size:27px">Roll-On</div>
    <div class="line volume" style="top:483px">10 ml / .34 fl oz</div>
  </section>

  <section class="label label--wide label--scrub">
    <div class="foliage foliage--left" role="img" aria-label="Leafy vine illustration along the left edge"></div>
    <div class="foliage foliage--right" role="img" aria-label="Leafy vine illustration along the right edge"></div>
    <span class="brand-dot" style="top:39px"></span>
    <div class="line brand" style="top:88px">Marisol Glade</div>
    <div class="line product-name" style="top:193px">Raw Honey &amp; Ginger</div>
    <div class="line product-type" style="top:268px">Mineral Body Scrub</div>
    <div class="line net-weight" style="top:383px">Net wt 8 oz</div>
  </section>

  <section class="label label--seal">
    <span class="brand-dot" style="top:128px"></span>
    <div class="line brand" style="top:187px">Marisol Glade</div>
  </section>

</main>
</body>
</html>
```